Copperleaf Motorized Shade Business Card

Hello, we've had our logo made. Now we are looking for a clean and cool looking business card. One side can just be the logo with any design elements that might look good with it. The other side will be Name, Phone Number and Email. There will not be an address on the card.

```html
<!DOCTYPE html>
<html lang="en">
<head>
<meta charset="utf-8">
<title>Copperleaf Motorized Shade – Business Card</title>
<link rel="stylesheet" href="https://fonts.googleapis.com/css2?family=Roboto+Condensed:wght@700&family=Questrial&family=Roboto:wght@400&display=swap">
<style>
  :root {
    --backdrop: #1f4777;
    --card-front: #1d4a80;
    --card-front-edge: #1a4275;
    --card-back: #fbfbfb;
    --navy: #1d3f73;
    --cyan: #19a3e2;
    --yellow: #f2b51d;
    --grey-text: #5f6266;
  }
  * { margin: 0; padding: 0; box-sizing: border-box; }
  html, body {
    width: 1200px;
    height: 986px;
    overflow: hidden;
    background: var(--backdrop);
  }
  .canvas {
    position: relative;
    width: 1200px;
    height: 986px;
  }
  .card {
    position: absolute;
    left: 341px;
    width: 518px;
    height: 296px;
    overflow: hidden;
  }
  .card-front {
    top: 160px;
    background: radial-gradient(ellipse at 50% 40%, var(--card-front) 0%, var(--card-front-edge) 100%);
    display: flex;
    align-items: center;
    justify-content: center;
  }
  .brand {
    display: flex;
    align-items: center;
    gap: 12px;
  }
  .brand-square {
    width: 22px;
    height: 22px;
    background: var(--yellow);
  }
  .brand-name {
    font-family: "Roboto Condensed", sans-serif;
    font-weight: 700;
    font-size: 24px;
    letter-spacing: 2px;
    color: var(--cyan);
    text-transform: uppercase;
  }
  .card-back {
    top: 529px;
    background: var(--card-back);
  }
  .identity {
    position: absolute;
    right: 282px;
    top: 131px;
    text-align: right;
  }
  .person-name {
    font-family: "Roboto Condensed", sans-serif;
    font-weight: 700;
    font-size: 27px;
    line-height: 1;
    color: var(--cyan);
    text-transform: uppercase;
  }
  .person-role {
    font-family: "Roboto", sans-serif;
    font-size: 18px;
    line-height: 1;
    margin-top: 8px;
    color: var(--grey-text);
  }
  .divider {
    position: absolute;
    left: 252px;
    top: 132px;
    width: 2px;
    height: 56px;
    background: var(--yellow);
  }
  .contacts {
    position: absolute;
    left: 270px;
    top: 131px;
    list-style: none;
  }
  .contact {
    display: flex;
    align-items: center;
    gap: 8px;
    height: 21px;
    font-family: "Questrial", sans-serif;
    font-size: 14px;
    color: var(--grey-text);
  }
  .contact svg { width: 13px; height: 13px; fill: var(--yellow); flex: none; }
  .stripe {
    position: absolute;
    left: 0;
    bottom: 0;
    width: 100%;
    height: 9px;
    display: flex;
  }
  .stripe span { flex: 1; }
  .stripe .navy { background: var(--navy); }
  .stripe .cyan { background: var(--cyan); }
  .stripe .yellow { background: var(--yellow); }
</style>
</head>
<body>
<main class="canvas">
  <section class="card card-front">
    <div class="brand">
      <span class="brand-square"></span>
      <span class="brand-name">Copperleaf Motorized Shade</span>
    </div>
  </section>

  <section class="card card-back">
    <div class="identity">
      <p class="person-name">Dana Whitfield</p>
      <p class="person-role">Director</p>
    </div>
    <div class="divider"></div>
    <ul class="contacts">
      <li class="contact">
        <svg viewBox="0 0 24 24"><path d="M6.6 10.8a15 15 0 0 0 6.6 6.6l2.2-2.2a1 1 0 0 1 1-.25 11.4 11.4 0 0 0 3.6.57 1 1 0 0 1 1 1V20a1 1 0 0 1-1 1A17 17 0 0 1 3 4a1 1 0 0 1 1-1h3.5a1 1 0 0 1 1 1c0 1.25.2 2.45.57 3.57a1 1 0 0 1-.25 1z"/></svg>
        555 014 2290
      </li>
      <li class="contact">
        <svg viewBox="0 0 24 24"><path d="M2 5h20v14H2z M2 6l10 7 10-7" fill="none" stroke="#f2b51d" stroke-width="0"/><path d="M2 5h20v2l-10 6L2 7z"/><path d="M2 9l10 6 10-6v10H2z"/></svg>
        info@copperleafshade.com
      </li>
      <li class="contact">
        <svg viewBox="0 0 24 24"><circle cx="12" cy="12" r="9.5" fill="none" stroke="#f2b51d" stroke-width="2"/><ellipse cx="12" cy="12" rx="4" ry="9.5" fill="none" stroke="#f2b51d" stroke-width="2"/><path d="M2.5 12h19M4 7h16M4 17h16" stroke="#f2b51d" stroke-width="1.6"/></svg>
        www.copperleafshade.com
      </li>
    </ul>
    <div class="stripe">
      <span class="navy"></span>
      <span class="cyan"></span>
      <span class="yellow"></span>
    </div>
  </section>
</main>
</body>
</html>
```